Letterhead Design for Law Firm that Specializes in Property Damage Litigation

We are looking for a redesign of our letterhead. Our current letterhead lists all of our current staff members and we'd like to come up with a design that does NOT list all of the staff members so that it does not need to be updated with every newly hired employee. Must be in editable format.

We are a law firm that specializes in property damage, so we need something that is professional, yet modern. The final design should use our existing logo and should use a blue color scheme (alternate colors would be gray, black, and white).

Industry/Entity Type

Legal

Colors
0054AA
0677BA
7BADD7
CADEEF
E8F1F8

```html
<!DOCTYPE html>
<html lang="en">
<head>
<meta charset="utf-8">
<title>Hartwell Lange &amp; Morrow Letterhead</title>
<link href="https://fonts.googleapis.com/css2?family=Barlow:wght@400;500&family=Roboto:wght@400;500;700&family=Roboto+Condensed:wght@400;700&display=swap" rel="stylesheet">
<style>
  :root {
    --navy: #00305f;
    --ink: #2b2b2b;
    --grey-band: #b7b7b7;
    --grey-text: #4a4a4a;
    --backdrop: #dcdcdc;
    --paper: #ffffff;
  }
  html, body {
    margin: 0; padding: 0;
    width: 1200px; height: 1200px;
    overflow: hidden;
    background: var(--backdrop);
  }
  .letterhead {
    position: absolute;
    left: 190px; top: 20px;
    width: 820px; height: 1160px;
    background: var(--paper);
    font-family: "Barlow", sans-serif;
    color: var(--ink);
    overflow: hidden;
  }
  .side-band { position: absolute; left: 0; top: 0; width: 31px; height: 100%; }
  .side-band .upper { position: absolute; top: 0; left: 0; width: 31px; height: 377px; background: var(--grey-band); }
  .side-band .marker { position: absolute; top: 384px; left: 8px; width: 15px; height: 15px; background: var(--navy); }
  .side-band .lower { position: absolute; top: 406px; bottom: 0; left: 0; width: 31px; background: var(--navy); }

  .firm-name {
    position: absolute; left: 82px; top: 48px;
    display: flex; align-items: center; gap: 14px;
  }
  .firm-name .mark { width: 52px; height: 52px; background: var(--navy); }
  .firm-name .words {
    font-family: "Barlow", sans-serif; font-weight: 500;
    color: var(--navy); font-size: 25px; line-height: 26px;
    letter-spacing: 1.5px; text-transform: uppercase;
  }
  .tagline {
    position: absolute; left: 82px; top: 136px;
    font-family: "Barlow", sans-serif; font-weight: 500;
    font-size: 10.5px; letter-spacing: 2.6px; color: var(--grey-text);
  }
  .contact {
    position: absolute; right: 64px; top: 114px;
    font-family: "Roboto", sans-serif; font-size: 14.5px;
    color: var(--grey-text); text-align: right; line-height: 19px;
  }
  .contact .item { display: flex; align-items: center; justify-content: flex-end; gap: 5px; }
  .contact strong { color: var(--navy); font-weight: 700; }
  .contact svg { width: 11px; height: 11px; }

  .recipient {
    position: absolute; left: 82px; top: 208px;
    font-size: 14.5px; line-height: 18.2px; letter-spacing: 0.4px;
  }
  .salutation { position: absolute; left: 82px; top: 336px; font-size: 14.5px; letter-spacing: 0.4px; }
  .body-copy {
    position: absolute; left: 82px; top: 381px; width: 679px;
    font-size: 14px; line-height: 24px; letter-spacing: 0.35px;
  }
  .body-copy p { margin: 0; text-align: justify; text-align-last: left; }

  .signature {
    position: absolute; left: 82px; top: 755px; width: 270px; height: 52px;
    background: linear-gradient(90deg, #efefef, #f6f6f6);
  }
  .closing { position: absolute; left: 82px; top: 816px; font-size: 14.5px; letter-spacing: 0.4px; }

  .offices {
    position: absolute; left: 82px; top: 1062px;
    display: flex; gap: 22px;
    font-family: "Roboto Condensed", sans-serif; font-size: 10px; line-height: 13.2px;
  }
  .office { border-left: 1px solid var(--navy); padding-left: 8px; }
  .office h3 { margin: 0 0 3px; font-size: 10.5px; font-weight: 700; color: var(--navy); }
  .office .line { display: flex; align-items: center; gap: 2px; color: #222; }
  .office .line svg { width: 8px; height: 8px; }
  .office .address { color: var(--navy); }
</style>
</head>
<body>
<div class="letterhead">
  <div class="side-band">
    <div class="upper"></div>
    <div class="marker"></div>
    <div class="lower"></div>
  </div>

  <div class="firm-name">
    <div class="mark"></div>
    <div class="words">Hartwell<br>Lange &amp;<br>Morrow</div>
  </div>
  <div class="tagline">THE PROPERTY DAMAGE ATTORNEYS</div>

  <div class="contact">
    <div class="item">555.010.2000
      <svg viewBox="0 0 24 24"><path fill="#00305f" d="M6.6 10.8a15.1 15.1 0 0 0 6.6 6.6l2.2-2.2a1 1 0 0 1 1-.25 11.4 11.4 0 0 0 3.6.57 1 1 0 0 1 1 1V20a1 1 0 0 1-1 1A17 17 0 0 1 3 4a1 1 0 0 1 1-1h3.5a1 1 0 0 1 1 1c0 1.25.2 2.45.57 3.57a1 1 0 0 1-.25 1z"/></svg>
    </div>
    <div class="item">www.<strong>hlmlaw</strong>.example
      <svg viewBox="0 0 24 24"><circle cx="12" cy="12" r="9.5" fill="none" stroke="#00305f" stroke-width="2"/><path d="M2.5 12h19M12 2.5c3 3 3 16 0 19M12 2.5c-3 3-3 16 0 19" fill="none" stroke="#00305f" stroke-width="1.6"/></svg>
    </div>
  </div>

  <div class="recipient">
    Mr. John Doe<br>President<br>Strategy Accountants<br>111 Street Name,<br>City State, 12345
  </div>

  <div class="salutation">Dear :</div>

  <div class="body-copy">
    <p>Lorem ipsum dolor sit amet, consectetur adipiscing elit. Aenean ut ipsum eget massa hendrerit vestibulum vel in velit. Donec pretium neque velit.</p>
    <p>Aliquam porta lectus nec mauris ornare venenatis. Vivamus non est turpis, et cursus sem. Mauris vehicula erat in diam auctor at bibendum nisl lacinia.</p>
    <p>Morbi imperdiet neque vehicula nunc convallis gravida. Vestibulum iaculis pretium placerat. Integer consequat, est sit amet facilisis eleifend, nibh nibh varius orci, eget dapibus arcu dui non purus. Pellentesque in magna mauris. Duis enim sapien, dictum vitae condimentum a, pulvinar vel lacus. Mauris et molestie nibh. Vestibulum vitae nulla at metus elementum porta sit amet interdum elit. Nulla sollicitudin neque eu nulla volutpat congue.</p>
    <p>Etiam pellentesque, velit id dapibus fermentum, turpis sapien ornare dui, ac tincidunt ligula odio congue purus. Nunc sed ante dui, in porta lectus. Cras nec sem lorem. In hac habitasse platea dictumst. Maecenas id diam quis dui porta tristique. Sed id egestas felis. Donec ullamcorper mattis posuere. Phasellus fermentum eleifend tortor vel dapibus. Vestibulum ante ipsum.</p>
  </div>

  <div class="signature" role="img" aria-label="Handwritten signature of the sending attorney"></div>
  <div class="closing">Sincerely,</div>

  <div class="offices">
    <div class="office">
      <h3>PHILADELPHIA OFFICE</h3>
      <div class="line"><svg viewBox="0 0 24 24"><path fill="#00305f" d="M6.6 10.8a15.1 15.1 0 0 0 6.6 6.6l2.2-2.2a1 1 0 0 1 1-.25 11.4 11.4 0 0 0 3.6.57 1 1 0 0 1 1 1V20a1 1 0 0 1-1 1A17 17 0 0 1 3 4a1 1 0 0 1 1-1h3.5a1 1 0 0 1 1 1c0 1.25.2 2.45.57 3.57a1 1 0 0 1-.25 1z"/></svg>: 555.010.2000</div>
      <div class="line"><svg viewBox="0 0 24 24"><rect x="6" y="2" width="12" height="6" fill="#00305f"/><rect x="2" y="9" width="20" height="9" rx="2" fill="#00305f"/><rect x="6" y="15" width="12" height="7" fill="#00305f"/></svg>: 555.010.2100</div>
      <div class="address">220 Harbor Street,<br>Suite 410 Philadelphia, PA 19106</div>
    </div>
    <div class="office">
      <h3>NEW JERSEY OFFICE</h3>
      <div class="line"><svg viewBox="0 0 24 24"><path fill="#00305f" d="M6.6 10.8a15.1 15.1 0 0 0 6.6 6.6l2.2-2.2a1 1 0 0 1 1-.25 11.4 11.4 0 0 0 3.6.57 1 1 0 0 1 1 1V20a1 1 0 0 1-1 1A17 17 0 0 1 3 4a1 1 0 0 1 1-1h3.5a1 1 0 0 1 1 1c0 1.25.2 2.45.57 3.57a1 1 0 0 1-.25 1z"/></svg>: 555.010.3000</div>
      <div class="line"><svg viewBox="0 0 24 24"><rect x="6" y="2" width="12" height="6" fill="#00305f"/><rect x="2" y="9" width="20" height="9" rx="2" fill="#00305f"/><rect x="6" y="15" width="12" height="7" fill="#00305f"/></svg>: 555.010.2100</div>
      <div class="address">85 Orchard Road<br>Suite 120, Cherry Hill, NJ 08002</div>
    </div>
  </div>
</div>
</body>
</html>
```